Business Card Design Project - KLB

I am looking for a more sophisticated card design for my company,
"The Kestrel Bureau"

We are a consultancy focused on strategy and change in Associations and professional organisations.

I am a lawyer and psychologist with a PhD and so am looking for something that communicates seriousness and credibility but also quirky creative solutions for strategic problems, which is my field of speciality.

I am looking for something that is quietly spoken, rather than loud colours ('credible' and 'creative' are the two adjectives that I think of as competing here).

I particularly like an embossed card style - heavy white card with plain white or white and black or white and grey text.

The key logo image for the company is a question mark and I am open to suggestions and ideas on design.

I have attached a file that includes a couple of styles that have caught my eye and my thoughts on them. Hopefully they communicate what I'm looking for.
Updates

Thank you for all the great suggestions and designs.

I really appreciated the effort and creative energy you put into your designs. I have now closed the project after selecting a design and advising the successful designer of the card that I am happy with.

Regards

Target Market(s)

Organisations (CEO's and Boards), Governments, Legal professionals, Membership Associations and aspiring professionals.

Industry/Entity Type

Lawyer

Requirements
Must have
• The key logo element is a question mark (?) and this needs to be incorporated.

Embossed style - cut outs or other design ideas interest me too.

The attached file has a number of sample ideas and comments on each one that I like.
Should not have
• I like crisp, modern fonts (Myriads etc...) and do not like embellished fonts or Times etc...

```html
<!DOCTYPE html>
<html lang="en">
<head>
<meta charset="utf-8">
<title>The Kestrel Bureau – Business Cards</title>
<link rel="stylesheet" href="https://fonts.googleapis.com/css2?family=Source+Sans+3:wght@400;600;700&display=swap">
<style>
  :root {
    --stage: #ececec;
    --ink: #111111;
    --card-black: #0b0b0b;
    --card-grey: #5a5a5a;
    --paper: #ffffff;
    --text-dark: #1a1a1a;
    --text-light: #ffffff;
  }
  * { box-sizing: border-box; margin: 0; padding: 0; }
  html, body {
    width: 1200px; height: 900px; overflow: hidden;
    background: var(--stage);
    font-family: "Source Sans 3", "Myriad Pro", Arial, sans-serif;
  }
  .stage { position: relative; width: 1200px; height: 900px; }

  .card {
    position: absolute;
    width: 512px; height: 318px;
    overflow: hidden;
    box-shadow: 0 2px 6px rgba(0,0,0,0.18);
  }

  /* Brand lock-up: plain circle + name, one weight, one colour */
  .brand { position: absolute; color: var(--text-light); font-weight: 700; text-transform: uppercase; }
  .brand-mark { border-radius: 50%; background: var(--text-light); }
  .brand-short { display: block; line-height: 0.9; letter-spacing: -1px; }
  .brand-full { display: block; line-height: 1.1; }

  /* Card 1 – contact card */
  .card-contact { left: 70px; top: 40px; background: var(--paper); }
  .card-contact .side-panel {
    position: absolute; left: 0; top: 0; width: 190px; height: 100%;
    background: radial-gradient(circle at 50% 40%, #3a3a3a 0%, var(--card-black) 75%);
  }
  .card-contact .brand-mark { position: absolute; left: 40px; top: 22px; width: 90px; height: 90px; }
  .card-contact .brand { left: 40px; top: 130px; }
  .card-contact .brand-short { font-size: 58px; }
  .card-contact .brand-full { font-size: 14px; }

  .contact { position: absolute; left: 220px; top: 96px; color: var(--text-dark); }
  .contact-name { font-size: 19px; font-weight: 700; }
  .contact-role { font-size: 15px; margin-bottom: 20px; }
  .contact-list { list-style: none; font-size: 13px; line-height: 1.55; }
  .contact-list .label { display: inline-block; width: 34px; font-weight: 600; }
  .contact-list .indent { padding-left: 34px; }

  /* Card 2 – brand front */
  .card-front {
    left: 624px; top: 136px;
    background: radial-gradient(ellipse at 50% 45%, var(--card-grey) 0%, #262626 55%, var(--card-black) 100%);
  }
  .card-front .brand-mark { position: absolute; left: 206px; top: 38px; width: 100px; height: 100px; }
  .card-front .brand { left: 0; width: 100%; top: 158px; text-align: center; }
  .card-front .brand-short { font-size: 80px; }
  .card-front .brand-full { font-size: 19px; }

  /* Card 3 – feature back */
  .card-feature {
    left: 226px; top: 484px;
    background: radial-gradient(ellipse at 75% 50%, #4a4a4a 0%, #1b1b1b 50%, var(--card-black) 100%);
  }
  .card-feature .feature-mark {
    position: absolute; left: -20px; top: -10px; width: 330px; height: 330px;
    border-radius: 50%; background: var(--text-light);
  }
  .card-feature .brand { left: 338px; top: 110px; }
  .card-feature .brand-short { font-size: 66px; }
  .card-feature .brand-full { font-size: 16px; }
</style>
</head>
<body>
<main class="stage">

  <section class="card card-contact">
    <div class="side-panel">
      <div class="brand-mark"></div>
      <div class="brand">
        <span class="brand-short">KLB</span>
        <span class="brand-full">The Kestrel Bureau</span>
      </div>
    </div>
    <div class="contact">
      <p class="contact-name">Dr. Mara Ellison</p>
      <p class="contact-role">Director</p>
      <ul class="contact-list">
        <li><span class="label">M ::</span>+61 400 271 946</li>
        <li><span class="label">P ::</span>+612 9555 0142</li>
        <li><span class="label">E ::</span>mara@kestrelbureau.com.au</li>
        <li><span class="label">PO::</span>P.O. Box 1184, Glenhaven</li>
        <li class="indent">Sydney, Australia</li>
      </ul>
    </div>
  </section>

  <section class="card card-front">
    <div class="brand-mark"></div>
    <div class="brand">
      <span class="brand-short">KLB</span>
      <span class="brand-full">The Kestrel Bureau</span>
    </div>
  </section>

  <section class="card card-feature">
    <div class="feature-mark"></div>
    <div class="brand">
      <span class="brand-short">KLB</span>
      <span class="brand-full">The Kestrel Bureau</span>
    </div>
  </section>

</main>
</body>
</html>
```